Powerpoint for consulting dentalpractices on management, improvement, and benchmarks

Fase 1: create 8-15 slides to be used for the model. The are the basic slideexamples for future presentation.
colour scheme and font types as in attachment for older powerpoint. Fonts, logo and colourscheme stay the same. Newer slidedeck contains newer ideas for new presentations. Smaller logo maybe better to be used for all slides. Normal logo for starting and end slide. Open for your inspiration and new suggestions
Fase 2 create slidemaster to enable us to create new slidedesks faster.

Target Market(s)

Dentalpractices (no dental images in powerpoint)

Industry/Entity Type

Dental practices

Font styles to use
Other font styles liked:
• Roobert for heading Normal Text Inter

Requirements
Must have
• Different slidemaster basic slides to quickly create slides with full slide pictures which still have a Molvaro touch. Content slides, slides with bullets and slides to show 3 -5 subjects
Nice to have
• New styling element for recognition of brand
Should not have
• round edges, complex slide master

```html
<!DOCTYPE html>
<html lang="nl">
<head>
<meta charset="utf-8">
<title>Molvaro – presentatiereeks</title>
<link href="https://fonts.googleapis.com/css2?family=Inter:wght@400;500;600&family=Figtree:wght@500;600&display=swap" rel="stylesheet">
<style>
:root{
  --blue:#0b55a3;
  --blue-deep:#07468c;
  --blue-light:#3f7fc6;
  --green:#6cbd17;
  --ink:#4a4a4a;
  --page:#eaeaea;
  --stage:#e4e7ec;
  --white:#ffffff;
  --alert:#c0264a;
}
*{box-sizing:border-box;margin:0;padding:0}
html,body{width:679px;height:1200px;overflow:hidden}
body{background:var(--page);font-family:Inter,Arial,sans-serif;position:relative;color:var(--ink)}
.stage{position:absolute;left:0;top:0;width:679px;height:410px;background:linear-gradient(180deg,#dfe3e9,var(--stage))}
.brand-corner{position:absolute;left:556px;top:38px;font-family:Figtree,Inter,sans-serif;font-weight:600;font-size:26px;color:var(--blue);letter-spacing:-.5px}
.slide{position:absolute;width:682px;height:383px;overflow:hidden;background:var(--white);transform-origin:0 0}
.slide svg.bg{position:absolute;inset:0;width:682px;height:383px}
.abs{position:absolute}
.wordmark{font-family:Figtree,Inter,sans-serif;font-weight:600;color:var(--blue);font-size:34px;letter-spacing:-.5px;line-height:1}
.mini-mark{position:absolute;left:14px;bottom:14px;font-family:Figtree,Inter,sans-serif;font-weight:600;font-size:12px;color:var(--blue)}
.cover-title{font-family:Figtree,Inter,sans-serif;font-weight:500;color:var(--white);font-size:40px;line-height:41px;text-align:center;width:340px}
.cover-sub{color:var(--white);font-size:15px;text-align:center;width:340px}
.date-pill{background:var(--green);color:var(--white);font-size:8px;font-weight:600;letter-spacing:.6px;width:128px;height:14px;line-height:14px;text-align:center}
.url{font-size:7px;letter-spacing:1.4px;color:#777;font-weight:500}
.url-light{color:#fff}
.cover-url{top:22px}
.page-no{width:12px;height:12px;background:var(--green);color:#fff;font-size:6px;line-height:12px;text-align:center}
.page-no.blue{background:var(--blue)}
.heading{font-family:Figtree,Inter,sans-serif;font-weight:600;font-size:26px;color:var(--blue);left:33px;top:30px;white-space:nowrap}
.heading.on-blue{color:var(--white)}
.heading::after{content:"";display:block;width:30px;height:3px;background:var(--green);margin-top:3px}
.bullets{list-style:none}
.bullets li{font-size:14.5px;color:var(--ink);height:31px;display:flex;align-items:center;white-space:nowrap}
.bullets li::before{content:"";width:13px;height:13px;background:var(--green);margin-right:12px;flex:none}
.card-photo{width:250px;height:100px;border:2px solid #fff}
.card-title{font-family:Figtree,Inter,sans-serif;font-size:16px;color:var(--blue);font-weight:500}
.dot-list{list-style:none;font-size:8px;line-height:13px;color:#555}
.dot-list li::before{content:"";display:inline-block;width:3px;height:3px;background:var(--green);margin-right:10px;vertical-align:middle}
.asa{position:absolute;top:112px;width:144px;height:188px}
.asa svg{position:absolute;inset:0;width:144px;height:188px}
.asa h3{position:absolute;left:13px;top:48px;font-size:12px;font-weight:600;color:var(--blue);letter-spacing:-.3px}
.asa ul{position:absolute;left:10px;top:80px;width:126px;list-style:none;font-size:5.5px;line-height:6px;color:#fff}
.asa li{display:flex;margin-bottom:5px}
.asa li::before{content:"•";margin-right:8px}
.inr-table{position:absolute;left:34px;top:80px;width:272px;border-collapse:collapse;font-size:9px;text-align:center;color:#555}
.inr-table th{height:30px;color:#fff;font-weight:600}
.inr-table td{height:32px}
.inr-table tr:nth-child(odd) td{background:#f4f4f4}
.inr-table tr:nth-child(even) td{background:#e4e4e4}
.inr-table .col-a{background:var(--blue)}
.inr-table .col-b{background:var(--green)}
.inr-table tr.last td.col-a{background:var(--blue);color:#fff}
.inr-table tr.last td.col-b{background:var(--green);color:#fff}
.normal-range{position:absolute;left:34px;top:110px;width:272px;height:64px;border:2px solid var(--alert)}
.contact{color:#fff}
.contact h4{font-family:Figtree,Inter,sans-serif;font-size:14px;font-weight:600}
.contact .addr{font-size:7.5px;margin-top:6px}
.contact ul{list-style:none;margin-top:14px;font-size:9px}
.contact li{display:flex;align-items:center;height:20px}
.contact li svg{width:11px;height:11px;margin-right:10px}
</style>
</head>
<body>

<section class="stage">
  <div class="brand-corner">Molvaro</div>

  <div class="slide" style="left:99px;top:60px;transform:scale(.704)">
    <svg class="bg" viewBox="0 0 682 383" role="img" aria-label="Foto: handen die een rood hart vasthouden">
      <defs>
        <linearGradient id="photoA" x1="0" y1="0" x2="1" y2="1">
          <stop offset="0" stop-color="#5f7f3f"/><stop offset=".45" stop-color="#c9a08a"/><stop offset=".7" stop-color="#b98a72"/><stop offset="1" stop-color="#8ca06a"/>
        </linearGradient>
      </defs>
      <rect width="682" height="383" fill="url(#photoA)"/>
      <polygon points="330,0 682,0 682,245" fill="#fff"/>
      <polygon points="30,383 462,100 476,106 52,383" fill="#7aa8dd" opacity=".6"/>
      <polygon points="52,383 476,106 682,245 682,383" fill="var(--blue)"/>
    </svg>
    <div class="abs url url-light cover-url" style="left:22px">https://molvaro.nl</div>
    <div class="abs wordmark" style="left:515px;top:52px">Molvaro</div>
    <div class="abs cover-title" style="left:293px;top:206px">Taakdelegatie<br>en de controle</div>
    <div class="abs cover-sub" style="left:293px;top:296px">Tandartspraktijk Verhoeven</div>
    <div class="abs date-pill" style="left:399px;top:336px">December 19, 2022</div>
  </div>
</section>

<div class="slide" style="left:16px;top:428px;transform:scale(.4663)">
  <svg class="bg" viewBox="0 0 682 383" role="img" aria-label="Foto: handen die een rood hart vasthouden">
    <defs>
      <linearGradient id="photoB" x1="0" y1="0" x2="1" y2="1">
        <stop offset="0" stop-color="#5f7f3f"/><stop offset=".45" stop-color="#c9a08a"/><stop offset=".7" stop-color="#b98a72"/><stop offset="1" stop-color="#8ca06a"/>
      </linearGradient>
    </defs>
    <rect width="682" height="383" fill="url(#photoB)"/>
    <polygon points="310,0 682,0 682,235" fill="#fff"/>
    <polygon points="30,383 462,100 476,106 52,383" fill="#7aa8dd" opacity=".6"/>
    <polygon points="52,383 476,106 682,235 682,383" fill="var(--blue)"/>
  </svg>
  <div class="abs url url-light cover-url" style="left:22px">https://molvaro.nl</div>
  <div class="abs wordmark" style="left:515px;top:52px">Molvaro</div>
  <div class="abs cover-title" style="left:293px;top:206px">Taakdelegatie<br>en de controle</div>
  <div class="abs cover-sub" style="left:293px;top:296px">Tandartspraktijk Verhoeven</div>
  <div class="abs date-pill" style="left:399px;top:336px">December 19, 2022</div>
</div>

<div class="slide" style="left:345px;top:428px;transform:scale(.4663)">
  <svg class="bg" viewBox="0 0 682 383" role="img" aria-label="Foto: handen die een rood hart vasthouden">
    <defs>
      <linearGradient id="photoC" x1="1" y1="0" x2="0" y2="1">
        <stop offset="0" stop-color="#5f7f3f"/><stop offset=".45" stop-color="#c9a08a"/><stop offset=".7" stop-color="#b98a72"/><stop offset="1" stop-color="#8ca06a"/>
      </linearGradient>
    </defs>
    <rect width="682" height="383" fill="url(#photoC)"/>
    <polygon points="372,0 0,0 0,235" fill="#fff"/>
    <polygon points="652,383 220,100 206,106 630,383" fill="#7aa8dd" opacity=".6"/>
    <polygon points="630,383 206,106 0,235 0,383" fill="var(--blue)"/>
  </svg>
  <div class="abs url url-light cover-url" style="right:22px">https://molvaro.nl</div>
  <div class="abs wordmark" style="left:52px;top:52px">Molvaro</div>
  <div class="abs cover-title" style="left:49px;top:206px">Taakdelegatie<br>en de controle</div>
  <div class="abs cover-sub" style="left:49px;top:296px">Tandartspraktijk Verhoeven</div>
  <div class="abs date-pill" style="left:155px;top:336px">December 19, 2022</div>
</div>

<div class="slide" style="left:16px;top:618px;transform:scale(.4663)">
  <svg class="bg" viewBox="0 0 682 383" role="img" aria-label="Foto: hand die houten blokken als staafdiagram plaatst">
    <defs>
      <linearGradient id="photoD" x1="0" y1="0" x2="1" y2="1">
        <stop offset="0" stop-color="#f3f1ee"/><stop offset=".5" stop-color="#d9b48a"/><stop offset="1" stop-color="#c9a27a"/>
      </linearGradient>
    </defs>
    <polygon points="568,0 682,0 682,383 424,383" fill="url(#photoD)"/>
  </svg>
  <h2 class="abs heading">Risicofactoren</h2>
  <ul class="abs bullets" style="left:47px;top:126px">
    <li>Leeftijd</li><li>Beroep</li><li>Medicatie &amp; ziekte</li><li>Leef- en eetpatroon</li><li>Roken</li>
  </ul>
  <ul class="abs bullets" style="left:252px;top:126px">
    <li>Maagzuur</li><li>Life events</li><li>Externe factoren</li><li>Weinig fluoridegebruik</li>
  </ul>
  <div class="mini-mark">Molvaro</div>
  <div class="abs url" style="left:563px;top:359px">https://molvaro.nl</div>
  <div class="abs page-no" style="left:657px;top:356px">3</div>
</div>

<div class="slide" style="left:345px;top:618px;transform:scale(.4663)">
  <svg class="bg" viewBox="0 0 682 383" role="img" aria-label="Foto: citroen, houten lepel met blad en tabletten">
    <defs>
      <linearGradient id="photoE" x1="0" y1="0" x2="1" y2="1">
        <stop offset="0" stop-color="#f2f2f0"/><stop offset=".45" stop-color="#f0e2a8"/><stop offset=".75" stop-color="#d3ab72"/><stop offset="1" stop-color="#ecebe8"/>
      </linearGradient>
    </defs>
    <polygon points="568,0 682,0 682,383 424,383" fill="url(#photoE)"/>
  </svg>
  <h2 class="abs heading">Gevolgen van de risicofactoren</h2>
  <ul class="abs bullets" style="left:47px;top:125px">
    <li>Onvoldoende mondhygiëne</li><li>Tekort aan speeksel</li><li>Cariës</li><li>Erosie</li>
  </ul>
  <ul class="abs bullets" style="left:252px;top:156px">
    <li>Witte laesies</li><li>Gingivitis/Parodontitis</li><li>Hallitose</li>
  </ul>
  <div class="mini-mark">Molvaro</div>
  <div class="abs url" style="left:563px;top:359px">https://molvaro.nl</div>
  <div class="abs page-no" style="left:657px;top:356px">4</div>
</div>

<div class="slide" style="left:16px;top:807px;transform:scale(.4663)">
  <svg class="bg" viewBox="0 0 682 383" role="img" aria-label="Vervaagde achtergrondfoto in blauw">
    <defs>
      <linearGradient id="band" x1="0" y1="0" x2="1" y2="0">
        <stop offset="0" stop-color="var(--blue)"/><stop offset=".5" stop-color="#1c62ad"/><stop offset="1" stop-color="var(--blue)"/>
      </linearGradient>
    </defs>
    <rect width="682" height="152" fill="url(#band)"/>
  </svg>
  <h2 class="abs heading on-blue">Risicofactoren</h2>
  <div class="abs card-photo" role="img" aria-label="Foto: bloedglucosemeter, insulinepen en suikerklontjes" style="left:63px;top:100px;background:linear-gradient(135deg,#bcd7ea,#7fb0d6 50%,#e9eef2)"></div>
  <div class="abs card-photo" role="img" aria-label="Foto: boek met titel over het syndroom van Sjögren" style="left:368px;top:100px;background:linear-gradient(135deg,#c9c6bd,#2a2a2a 40%,#3b3a34 70%,#b08a2a)"></div>
  <div class="abs card-title" style="left:70px;top:207px">Type I of II</div>
  <ul class="abs dot-list" style="left:70px;top:237px">
    <li>Snel bloedend tandvlees</li><li>Droge mond</li><li>Meer eetmomenten (ook in de nacht)</li><li>Koolhydraten en suikers</li><li>Stabiel of niet?</li><li>Gebruik Insuline?</li>
  </ul>
  <div class="abs card-title" style="left:375px;top:207px">Vorm van reuma</div>
  <ul class="abs dot-list" style="left:375px;top:237px">
    <li>Ontsteking aan speekselklieren</li><li>Droge mond</li><li>Meer plakvorming</li>
  </ul>
  <div class="mini-mark">Molvaro</div>
  <div class="abs url" style="left:563px;top:359px">https://molvaro.nl</div>
  <div class="abs page-no" style="left:657px;top:356px">5</div>
</div>

<div class="slide" style="left:345px;top:807px;transform:scale(.4663)">
  <svg class="bg" viewBox="0 0 682 383" role="img" aria-label="Vervaagde achtergrondfoto in blauw">
    <defs>
      <linearGradient id="band2" x1="0" y1="0" x2="1" y2="0">
        <stop offset="0" stop-color="var(--blue)"/><stop offset=".5" stop-color="#1c62ad"/><stop offset="1" stop-color="var(--blue)"/>
      </linearGradient>
    </defs>
    <rect width="682" height="207" fill="url(#band2)"/>
  </svg>
  <h2 class="abs heading on-blue">Medische Anamnese</h2>
  <div class="asa" style="left:37px">
    <svg viewBox="0 0 144 188"><polygon points="0,24 144,0 144,73 0,73" fill="#fff"/><rect y="73" width="144" height="115" fill="var(--green)"/></svg>
    <h3>ASA I</h3>
    <ul><li>Gezonde patiënt.</li><li>Iedere behandeling mogelijk</li></ul>
  </div>
  <div class="asa" style="left:193px">
    <svg viewBox="0 0 144 188"><polygon points="0,24 144,0 144,73 0,73" fill="#fff"/><rect y="73" width="144" height="115" fill="var(--green)"/></svg>
    <h3>ASA II</h3>
    <ul><li>Lichte of matige systematische afwijkingen, die de dagelijkse activiteit van de patiënt niet belemmeren.</li><li>Enige beperkingen: dit impliceert beperking van behandelingsduur en stress, in combinatie met het treffen van profylactische maatregelen.</li></ul>
  </div>
  <div class="asa" style="left:349px">
    <svg viewBox="0 0 144 188"><polygon points="0,24 144,0 144,73 0,73" fill="#fff"/><rect y="73" width="144" height="115" fill="var(--green)"/></svg>
    <h3>ASA III</h3>
    <ul><li>Activiteit belemmerende systematische afwijkingen.</li><li>Routine behandelingen vaak wel mogelijk. Uitvoeren uitgebreide behandeling met eigen tandarts onder voorwaarden</li></ul>
  </div>
  <div class="asa" style="left:505px">
    <svg viewBox="0 0 144 188"><polygon points="0,24 144,0 144,73 0,73" fill="#fff"/><rect y="73" width="144" height="115" fill="var(--green)"/></svg>
    <h3>ASA IV</h3>
    <ul><li>levensbedreigende systematische afwijkingen.</li><li>Alleen noodvoorzieningen.</li></ul>
  </div>
  <div class="mini-mark">Molvaro</div>
  <div class="abs url" style="left:563px;top:359px">https://molvaro.nl</div>
  <div class="abs page-no blue" style="left:657px;top:356px">6</div>
</div>

<div class="slide" style="left:16px;top:997px;transform:scale(.4663)">
  <svg class="bg" viewBox="0 0 682 383" role="img" aria-label="Vervaagde achtergrondfoto in blauw">
    <rect x="341" width="341" height="383" fill="var(--blue)"/>
    <rect x="341" y="120" width="341" height="150" fill="#1c62ad" opacity=".6"/>
  </svg>
  <table class="inr-table">
    <tr><th class="col-a">INR</th><th class="col-b">Stollingspercentage</th></tr>
    <tr><td>1.0</td><td>100</td></tr>
    <tr><td>1.2</td><td>50</td></tr>
    <tr><td>1.8</td><td>20</td></tr>
    <tr><td>2.5</td><td>12</td></tr>
    <tr><td>3.0</td><td>9</td></tr>
    <tr class="last"><td class="col-a">meer dan 4.0</td><td class="col-b">minder dan 5</td></tr>
  </table>
  <div class="normal-range"></div>
  <svg class="abs" style="left:280px;top:280px" width="120" height="80" viewBox="0 0 120 80">
    <path d="M8 66 C45 82 85 70 102 22" fill="none" stroke="var(--green)" stroke-width="7" stroke-linecap="round"/>
    <polygon points="90,26 106,4 116,32" fill="var(--green)"/>
  </svg>
  <div class="abs" style="left:361px;top:92px;width:300px;text-align:center;color:#fff;font-family:Figtree,Inter,sans-serif;font-weight:500;font-size:24px;line-height:27px">INR en<br>Stollingsfactoren<br>Percentage</div>
  <div class="abs" style="left:496px;top:182px;width:30px;height:3px;background:var(--green)"></div>
  <div class="abs" style="left:361px;top:244px;width:300px;text-align:center;color:#fff;font-size:12px">Een INR van 1.0-1.2 is normaal</div>
  <div class="mini-mark">Molvaro</div>
  <div class="abs url url-light" style="left:563px;top:359px">https://molvaro.nl</div>
  <div class="abs page-no" style="left:657px;top:356px">7</div>
</div>

<div class="slide" style="left:345px;top:997px;transform:scale(.4663)">
  <svg class="bg" viewBox="0 0 682 383" role="img" aria-label="Foto: glazen kantoorgebouw tegen blauwe lucht">
    <defs>
      <linearGradient id="tower" x1="0" y1="0" x2="1" y2="1">
        <stop offset="0" stop-color="#e8f1f8"/><stop offset=".4" stop-color="#4d9bd6"/><stop offset="1" stop-color="#1a5c9c"/>
      </linearGradient>
    </defs>
    <polygon points="320,0 682,0 682,383 520,383" fill="url(#tower)"/>
    <polygon points="0,383 0,285 248,108 640,383" fill="var(--blue)"/>
  </svg>
  <div class="abs wordmark" style="left:52px;top:45px">Molvaro</div>
  <div class="abs contact" style="left:120px;top:222px">
    <h4>Contactgegevens</h4>
    <p class="addr">Berkenlaan 12, 4817 KD Voorstad</p>
    <ul>
      <li><svg viewBox="0 0 12 12"><path d="M2.5 1 L4.5 1 L5.5 4 L4 5 C4.8 6.6 5.6 7.4 7 8 L8 6.5 L11 7.5 L11 9.5 C11 10.3 10.3 11 9.5 11 C5 10.6 1.4 7 1 2.5 C1 1.7 1.7 1 2.5 1Z" fill="#fff"/></svg>30458127</li>
      <li><svg viewBox="0 0 12 12"><circle cx="6" cy="6" r="2.2" fill="none" stroke="#fff" stroke-width="1.2"/><path d="M8.2 6 L8.2 7.2 C8.2 8.6 10.8 8.6 10.8 6 A4.8 4.8 0 1 0 8.4 10.2" fill="none" stroke="#fff" stroke-width="1.2"/></svg>info@molvaro.nl</li>
      <li><svg viewBox="0 0 12 12"><circle cx="6" cy="6" r="5" fill="none" stroke="#fff" stroke-width="1"/><ellipse cx="6" cy="6" rx="2.2" ry="5" fill="none" stroke="#fff" stroke-width="1"/><path d="M1 6 H11 M2 3.5 H10 M2 8.5 H10" stroke="#fff" stroke-width="1"/></svg>https://molvaro.nl</li>
    </ul>
  </div>
</div>

</body>
</html>
```